VORLEN Website Design

We need a website designed for our company VORLEN. We are a luxury lifestyle club that will provide benefits and services for our members. The site should be clean & sleek, preferably using black and white (or darker colors). (example sites: brimvale.example, tusko.example)

Here is a link of a sample page I did using wix. (https://pelmundry4.sitebuild.example/mypage) This can be used to get a general idea.

Target Market(s)

Upper Middle Class in the United States

Number of Pages Required

5+ page

Font styles to use
Sans Serif
Other font styles liked:
• Arial (or other similar fonts)

Requirements
Must have
• A clean design that is eye-catching and speaks to our company.
Nice to have
• Ideas for copy.

```html
<!DOCTYPE html>
<html lang="en">
<head>
<meta charset="utf-8">
<title>VORLEN</title>
<link rel="stylesheet" href="https://fonts.googleapis.com/css2?family=Montserrat:wght@400;500&display=swap">
<style>
  :root {
    --ink: #000000;
    --bar: #161616;
    --panel: rgba(14, 14, 14, 0.96);
    --paper: #ffffff;
    --text-light: #ffffff;
    --text-dark: #222222;
    --sky-top: #3a2233;
    --sky-mid: #8a5a72;
    --sky-low: #d98a7e;
    --photo-dark: #1b1b1b;
    --photo-mid: #6a6a6a;
  }
  * { margin: 0; padding: 0; box-sizing: border-box; }
  html, body { width: 670px; height: 1200px; overflow: hidden; background: var(--paper); }
  body { position: relative; font-family: "Montserrat", Arial, sans-serif; color: var(--text-light); }

  .site-header { position: absolute; top: 0; left: 0; width: 670px; height: 35px; background: var(--bar); }
  .brand { position: absolute; left: 132px; top: 8px; font-size: 15px; font-weight: 400; letter-spacing: 0.5px; }
  .main-nav a { position: absolute; top: 13px; font-size: 6.6px; color: var(--text-light); text-decoration: none; letter-spacing: 0.2px; }

  .hero-photo { position: absolute; top: 35px; left: 0; width: 670px; height: 293px;
    background: linear-gradient(180deg, var(--sky-top) 0%, var(--sky-mid) 45%, var(--sky-low) 80%, #2a1a22 100%); }

  .feature-card { position: absolute; left: 288px; top: 172px; width: 319px; height: 283px; background: var(--paper);
    padding: 4px; box-shadow: 0 2px 8px rgba(0,0,0,0.25); }
  .feature-photo { width: 100%; height: 100%;
    background: linear-gradient(160deg, var(--photo-mid) 0%, #3a3a3a 40%, var(--photo-dark) 100%); }

  .intro-panel { position: absolute; left: 115px; top: 282px; width: 242px; height: 190px; background: var(--panel);
    box-shadow: 0 3px 8px rgba(0,0,0,0.35); text-align: right; padding: 32px 19px 0 20px; }
  .intro-title { font-size: 15px; font-weight: 500; letter-spacing: 0.3px; }
  .intro-copy { margin-top: 17px; font-size: 5.9px; line-height: 8.4px; }
  .intro-copy + .intro-copy { margin-top: 8px; }
  .apply-button { position: absolute; left: 141px; top: 140px; width: 82px; height: 19px; border-radius: 10px;
    background: var(--paper); color: var(--text-dark); font-size: 6.4px; line-height: 19px; text-align: center; }

  .services { position: absolute; top: 518px; left: 0; width: 670px; height: 682px; background: var(--ink); }
  .services-title { position: absolute; top: 49px; width: 100%; text-align: center; font-size: 14.5px; font-weight: 400; letter-spacing: 0.3px; }
  .service { position: absolute; width: 150px; text-align: center; }
  .service svg { display: block; margin: 0 auto; width: 56px; height: 56px; fill: none; stroke: var(--text-light); stroke-width: 2; stroke-linecap: round; stroke-linejoin: round; }
  .service-name { display: block; font-size: 6.4px; letter-spacing: 0.1px; }

  .social-links { position: absolute; top: 633px; left: 281px; display: flex; gap: 2.6px; }
  .social-links span { width: 13px; height: 13px; border-radius: 2px; background: var(--text-light); }
  .copyright { position: absolute; top: 662px; width: 100%; text-align: center; font-size: 6px; }
</style>
</head>
<body>
  <header class="site-header">
    <div class="brand">VORLEN</div>
    <nav class="main-nav">
      <a style="left:280px">HOME</a>
      <a style="left:318px">ABOUT</a>
      <a style="left:360px">SERVICES AND BENEFITS</a>
      <a style="left:458px">APPLY</a>
      <a style="left:496px">CONTACT US</a>
    </nav>
  </header>

  <div class="hero-photo" role="img" aria-label="Palm trees silhouetted against a pink and purple sunset over a pool"></div>

  <div class="feature-card">
    <div class="feature-photo" role="img" aria-label="Black and white photo of a dining lounge overlooking a city skyline at night"></div>
  </div>

  <section class="intro-panel">
    <h1 class="intro-title">WE ARE VORLEN</h1>
    <p class="intro-copy">Built in the image of a"Multi-Family Office", VORLEN provides members with access to just about any service, experience, and event desirable.</p>
    <p class="intro-copy">VORLEN is truly the most exclusive lifestyle club out there.</p>
    <a class="apply-button">Apply</a>
  </section>

  <section class="services">
    <h2 class="services-title">SERVICES AND BENEFITS</h2>

    <div class="service" style="left:96px;top:122px">
      <svg viewBox="0 0 56 56"><rect x="2" y="4" width="34" height="22"/><circle cx="19" cy="15" r="6"/><rect x="32" y="20" width="20" height="32" rx="2"/><rect x="36" y="24" width="12" height="6"/><path d="M37 36h2M43 36h2M37 42h2M43 42h2M37 48h2M43 48h2M6 52V40M12 52V34M18 52V42M24 52V38"/></svg>
      <span class="service-name" style="margin-top:10px">ACCOUNTING SERVICES</span>
    </div>
    <div class="service" style="left:263px;top:122px">
      <svg viewBox="0 0 56 56"><path d="M2 40h8l10-4h12a3 3 0 0 1 0 6H22M32 42l14-6a3 3 0 0 1 3 5l-17 9H10M2 52h8V36"/><path d="M30 34V18M30 22c0-10 10-14 20-16-2 10-8 16-20 16zM30 28c-2-6-8-8-14-8 0 6 6 10 14 8z"/></svg>
      <span class="service-name" style="margin-top:10px">INVESTMENT SERVICES</span>
    </div>
    <div class="service" style="left:429px;top:122px">
      <svg viewBox="0 0 56 56"><path d="M28 6v44M18 50h20M10 14h36M14 14L6 32h16zM42 14l-8 18h16zM6 32a8 6 0 0 0 16 0M34 32a8 6 0 0 0 16 0"/></svg>
      <span class="service-name" style="margin-top:10px">LAWYER SERVICES</span>
    </div>

    <div class="service" style="left:95px;top:268px">
      <svg viewBox="0 0 56 56"><path d="M4 52h48M8 52V36l10-8 10 8M6 38l12-10M22 52V22l14-12 14 12v30M20 24l16-14 16 14"/><rect x="12" y="42" width="10" height="10"/><rect x="30" y="28" width="10" height="8"/><rect x="30" y="40" width="10" height="8"/><path d="M35 28v8M35 40v8"/></svg>
      <span class="service-name" style="margin-top:9px">REAL ESTATE SERVICES</span>
    </div>
    <div class="service" style="left:263px;top:268px">
      <svg viewBox="0 0 56 56"><path d="M12 10c-6 4-6 14 0 24s16 18 24 18l4-4-6-6-5 3c-4-2-9-8-11-12l3-5-5-6z"/><circle cx="38" cy="18" r="14"/><path d="M38 17v9M38 12v.5"/></svg>
      <span class="service-name" style="margin-top:9px">24/7 CONCIERGE</span>
    </div>
    <div class="service" style="left:429px;top:268px">
      <svg viewBox="0 0 56 56"><path d="M48 6c3 0 3 3 1 5L38 22l6 26-4 3-10-20-9 9 1 8-3 2-4-9-9-4 2-3 8 1 9-9-20-10 3-4 26 6L45 7z"/></svg>
      <span class="service-name" style="margin-top:9px">PRIVATE JET TRAVEL</span>
    </div>

    <div class="service" style="left:95px;top:410px">
      <svg viewBox="0 0 56 56"><path d="M4 24h48v6a4 4 0 0 0 0 8v6H4v-6a4 4 0 0 0 0-8z"/><rect x="16" y="30" width="24" height="8"/><path d="M12 24l14-14 4 4a4 4 0 0 0 6 6l4 4"/></svg>
      <span class="service-name" style="margin-top:10px">EVENT ACCESS</span>
    </div>
    <div class="service" style="left:263px;top:410px">
      <svg viewBox="0 0 56 56"><path d="M4 28h48M4 28v22M52 28v22M4 50c4 0 4-4 8-4s4 4 8 4 4-4 8-4 4 4 8-4 4 4 8 4 4-4 8-4M12 28v20M22 28v20M34 28v20M44 28v20"/><path d="M14 28V14l2-4V4M18 28V18M34 22a10 10 0 0 1 20 0zM44 12v-2"/></svg>
      <span class="service-name" style="margin-top:10px">PRIVATE EVENTS</span>
    </div>
    <div class="service" style="left:429px;top:410px">
      <svg viewBox="0 0 56 56"><circle cx="28" cy="28" r="24"/><circle cx="28" cy="28" r="14"/><circle cx="28" cy="28" r="8"/><circle cx="28" cy="28" r="3"/><circle cx="14" cy="20" r="2"/><circle cx="44" cy="12" r="2"/></svg>
      <span class="service-name" style="margin-top:10px">EXPERIENCES</span>
    </div>

    <div class="social-links" aria-label="Social links">
      <span></span><span></span><span></span><span></span><span></span><span></span><span></span>
    </div>
    <p class="copyright">© 2018 VORLEN</p>
  </section>
</body>
</html>
```